Internet Of Things brochure

Need to create a brochure with a common theme to our website and the last 2 pages of the attached file. All the contect is in the file that I have attached.
website www.norvalegroup.com.au

Industry/Entity Type

Internet

```html
<!DOCTYPE html>
<html lang="en">
<head>
<meta charset="utf-8">
<title>Smart Cities Initiative – Norvale Group</title>
<link rel="stylesheet" href="https://fonts.googleapis.com/css2?family=Michroma&family=Source+Sans+3:wght@400;600&display=swap">
<style>
  :root {
    --stage: #e6e6e6;
    --paper: #ffffff;
    --brand-blue: #1f4fb0;
    --telco-blue: #2a8fd8;
    --ink: #222222;
    --panel-top: #34214f;
    --panel-bottom: #1c4a86;
    --panel-text: #f2f2f7;
    --footer: #333333;
    --badge-top: #1b9ad8;
    --badge-bottom: #1560b8;
  }
  * { margin: 0; padding: 0; box-sizing: border-box; }
  html, body { width: 1200px; height: 1200px; overflow: hidden; }
  body { background: var(--stage); font-family: "Source Sans 3", Arial, sans-serif; }

  .flyer { position: absolute; left: 150px; top: 0; width: 901px; height: 1200px; background: var(--paper); overflow: hidden; }

  .hero-photo { position: absolute; left: 0; top: 0; width: 901px; height: 516px;
    background: linear-gradient(160deg, #f3eadf 0%, #e7d3bd 30%, #7c8fb4 62%, #2f3e6a 100%); }
  .header-band { position: absolute; left: 0; top: 0; width: 901px; height: 138px; background: rgba(255,255,255,0.82); }

  .partner-name { position: absolute; font-family: "Source Sans 3", Arial, sans-serif; font-weight: 400; line-height: 1; white-space: nowrap; display: flex; align-items: center; gap: 10px; }
  .partner-name .mark { display: inline-block; flex: none; }
  .brand-main { left: 70px; top: 56px; font-size: 25px; color: var(--brand-blue); font-weight: 600; }
  .brand-main .mark { width: 26px; height: 26px; background: var(--brand-blue); }
  .brand-telco { left: 262px; top: 48px; font-size: 24px; color: var(--telco-blue); line-height: 1.05; }
  .brand-telco .mark { width: 40px; height: 40px; border-radius: 50%; background: var(--telco-blue); }
  .brand-cloud { left: 500px; top: 50px; font-size: 28px; color: #1a1a1a; line-height: 1.0; text-align: right; }

  .intro { position: absolute; left: 0; top: 516px; width: 458px; height: 599px; background: var(--paper); }
  .intro-title { position: absolute; left: 39px; top: 42px; font-family: "Michroma", sans-serif; font-size: 20.5px; color: var(--brand-blue); letter-spacing: 0.2px; font-weight: 400; -webkit-text-stroke: 0.6px var(--brand-blue); }
  .intro-copy { position: absolute; left: 39px; top: 92px; width: 377px; font-size: 14.2px; line-height: 18px; color: var(--ink); text-align: justify; }
  .intro-copy p + p { margin-top: 18px; }

  .pillars { position: absolute; left: 458px; top: 516px; width: 443px; height: 599px; background: linear-gradient(180deg, var(--panel-top) 0%, #2a3268 50%, var(--panel-bottom) 100%); color: var(--panel-text); }
  .pillars-divider { position: absolute; left: 209px; top: 33px; width: 1px; height: 551px; background: rgba(255,255,255,0.7); }
  .pillar { position: absolute; width: 170px; }
  .pillar-head { display: flex; align-items: center; gap: 10px; height: 38px; }
  .pillar-icon { width: 40px; height: 38px; flex: none; }
  .pillar-title { font-size: 14.6px; font-weight: 600; line-height: 18px; text-transform: uppercase; }
  .pillar-text { margin-top: 10px; font-size: 13px; line-height: 16px; }

  .footer { position: absolute; left: 0; top: 1115px; width: 901px; height: 85px; background: var(--footer); color: #fff; }
  .contact-list { position: absolute; left: 157px; top: 26px; display: flex; gap: 24px; }
  .contact { font-size: 17px; display: flex; align-items: center; gap: 6px; white-space: nowrap; }
  .contact svg { width: 15px; height: 15px; flex: none; }

  .partner-badge { position: absolute; left: 40px; top: 1081px; width: 87px; height: 86px; border-radius: 3px; background: linear-gradient(160deg, var(--badge-top), var(--badge-bottom)); }
</style>
</head>
<body>
<main class="flyer">
  <div class="hero-photo" role="img" aria-label="Photo of three business people in suits reviewing a document at a meeting table"></div>

  <header class="header-band">
    <div class="partner-name brand-main"><span class="mark"></span>Norvale Group</div>
    <div class="partner-name brand-telco"><span class="mark"></span><span>Tallis Partner<br>Business</span></div>
    <div class="partner-name brand-cloud">Mercator<br>Partner</div>
  </header>

  <section class="intro">
    <h1 class="intro-title">SMART CITIES INITIATIVE</h1>
    <div class="intro-copy">
      <p>A smart city is an urban development vision to integrate multiple information and communication technology (ICT) and Internet of things (IoT) solutions in a secure fashion to manage a city's assets – the city's assets include, but are not limited to, local departments' information systems, schools, libraries, transportation systems, hospitals, power plants, water supply networks, waste management, law enforcement, and other community services. The goal of building a smart city is to improve quality of life by using urban informatics and technology to improve the efficiency of services and meet residents' needs. ICT allows city officials to interact directly with the community and the city infrastructure and to monitor what is happening in the city, how the city is evolving, and how to enable a better quality of life. Through the use of sensors integrated with real-time monitoring systems, data are collected from citizens and devices – then processed and analyzed. The information and knowledge gathered are keys to tackling inefficiency.</p>
      <p>Norvale Group has the ability and smarts to push these solutions forward. Norvale Digital and Norvale Group together with the partnership of Tallis and Mercator Cloud hosting all these systems, solutions and devices have never been easier and cost effective to deploy and capitalize on.</p>
    </div>
  </section>

  <section class="pillars">
    <div class="pillars-divider"></div>

    <article class="pillar" style="left:24px; top:29px;">
      <div class="pillar-head">
        <svg class="pillar-icon" viewBox="0 0 40 38" fill="none" stroke="#fff" stroke-width="1.5"><circle cx="20" cy="19" r="10"/><path d="M10 19h20M20 9v20M13 12l14 14M27 12L13 26"/><circle cx="20" cy="3" r="2"/><circle cx="20" cy="35" r="2"/><circle cx="4" cy="19" r="2"/><circle cx="36" cy="19" r="2"/></svg>
        <h2 class="pillar-title">Smart<br>Governance</h2>
      </div>
      <p class="pillar-text">Interconnected within-city and across-city governance, including ICT-enabled services and interactions between public and private sectors.</p>
    </article>

    <article class="pillar" style="left:246px; top:29px;">
      <div class="pillar-head">
        <svg class="pillar-icon" viewBox="0 0 40 38" fill="none" stroke="#fff" stroke-width="1.5"><circle cx="18" cy="19" r="15"/><path d="M3 19h30M18 4v30M7 10h22M7 28h22"/><ellipse cx="18" cy="19" rx="7" ry="15"/><circle cx="30" cy="24" r="7" fill="#fff"/><path d="M27 24h6M31 21l2 3-2 3" stroke="#2f2a5e"/></svg>
        <h2 class="pillar-title">Smart<br>Economy</h2>
      </div>
      <p class="pillar-text">Smart energy including renewables, ICT-enabled energy grids, pollution control and monitoring, green buildings and green urban planning.</p>
    </article>

    <article class="pillar" style="left:24px; top:224px;">
      <div class="pillar-head">
        <svg class="pillar-icon" viewBox="0 0 40 38" fill="none" stroke="#fff" stroke-width="1.5"><circle cx="21" cy="19" r="14"/><path d="M7 19h28M21 5v28"/><ellipse cx="21" cy="19" rx="6" ry="14"/><path d="M4 30c2-10 8-14 14-12-2 8-8 12-14 12z" fill="#fff"/></svg>
        <h2 class="pillar-title">Smart<br>Environment</h2>
      </div>
      <p class="pillar-text">Interconnected within-city and across-city governance, including ICT-enabled services and interactions between public and private sectors.</p>
    </article>

    <article class="pillar" style="left:246px; top:224px;">
      <div class="pillar-head">
        <svg class="pillar-icon" viewBox="0 0 40 38" fill="#fff" stroke="#fff" stroke-width="1.5"><circle cx="20" cy="9" r="5" fill="none"/><path d="M18 14h4v3h-4z"/><path d="M20 0v2M11 4l2 2M29 4l-2 2M9 10h2M29 10h2" fill="none"/><path d="M8 36v-8c0-5 5-8 12-8s12 3 12 8v8z"/><path d="M20 21l-2 6 2 5 2-5z" fill="#2f2a5e" stroke="none"/></svg>
        <h2 class="pillar-title">Smart<br>People</h2>
      </div>
      <p class="pillar-text">Those with e-skills, working in ICT-enabled roles, having access to education and training, human resources and capacity management.</p>
    </article>

    <article class="pillar" style="left:24px; top:413px;">
      <div class="pillar-head">
        <svg class="pillar-icon" viewBox="0 0 44 38" fill="none" stroke="#fff" stroke-width="1.8"><circle cx="9" cy="28" r="7"/><circle cx="35" cy="28" r="7"/><path d="M9 28l8-10h12l6 10M17 18l5 10h7M24 10l3 8"/><circle cx="27" cy="5" r="3" fill="#fff"/></svg>
        <h2 class="pillar-title">Smart<br>Mobility</h2>
      </div>
      <p class="pillar-text">ICT supported and integrated transport and logistics. Sustainable, safe and interconnected systems for public transport, cars, bicycles and pedestrians.</p>
    </article>

    <article class="pillar" style="left:246px; top:413px;">
      <div class="pillar-head">
        <svg class="pillar-icon" viewBox="0 0 40 38" fill="none" stroke="#fff" stroke-width="5"><path d="M5 6a28 28 0 0 1 28 28"/><path d="M5 17a17 17 0 0 1 17 17"/><circle cx="8" cy="31" r="4" fill="#fff" stroke="none"/></svg>
        <h2 class="pillar-title">Smart<br>Living</h2>
      </div>
      <p class="pillar-text">ICT supported and integrated transport and logistics. Sustainable, safe and interconnected systems for public transport, cars, bicycles and pedestrians.</p>
    </article>
  </section>

  <footer class="footer">
    <div class="contact-list">
      <div class="contact contact-phone">
        <svg viewBox="0 0 16 16" fill="none" stroke="#fff" stroke-width="1.5"><path d="M4 1l3 3-2 2c1 2 3 4 5 5l2-2 3 3-2 3C7 15 1 9 1 3z"/></svg>1300 555 019</div>
      <div class="contact contact-web">
        <svg viewBox="0 0 16 16" fill="none" stroke="#fff" stroke-width="1.3"><circle cx="8" cy="8" r="7"/><ellipse cx="8" cy="8" rx="3" ry="7"/><path d="M1 8h14"/></svg>norvalegroup.com.au</div>
      <div class="contact contact-address">
        <svg viewBox="0 0 16 16" fill="#fff"><path d="M8 0a5 5 0 0 1 5 5c0 4-5 11-5 11S3 9 3 5a5 5 0 0 1 5-5zm0 3a2 2 0 1 0 0 4 2 2 0 0 0 0-4z"/></svg>128 – 130 Harbour Road, Westmead, NSW, 2145</div>
    </div>
  </footer>

  <div class="partner-badge" role="img" aria-label="Partner certification badge"></div>
</main>
</body>
</html>
```